TopQuizLane needs a dashboard page designed

Redesign the dashboard shown in the provided images.

There are two images:

NOTE: The vocabulary navigation on the left will be a very long list of words 100s, so keep that in mind when you're designing both the vocab navigation and the expanded vocab popup.

In the dashboard.png picture, there needs to be a progress chart showing the word progress like the following: review 1(show it as completed) -> review 2(show the user they are here) -> review 3(unvisited) -> review 4(unvisited)

The do-not-design-this-page.png image is for your reference only. It is not to be designed. Use it to understand the overall look and feel of the website to help you create the best dashboard page possible.
Updates

Need extra days to review

Industry/Entity Type

Education English learning

Number of Pages Required

1 page

Requirements
Must have
• The main navigation and main header cannot change between pages. See the do-not-design page for the main navigateion and header.
Should not have
• Do not add a person profile. We will not have images of our users. Keep the icons in the main navigation as they are.

```html
<!DOCTYPE html>
<html lang="en">
<head>
<meta charset="utf-8">
<title>TopQuizLane – Vocabulary Dashboard</title>
<link href="https://fonts.googleapis.com/css2?family=Poppins:wght@400;500;600;700&display=swap" rel="stylesheet">
<style>
:root{
  --topbar:#1f2326;
  --rail:#272a2d;
  --sidebar:#2d3033;
  --sidebar-text:#c9c9c9;
  --sidebar-muted:#9a9a9a;
  --page:#e6e6e6;
  --card:#f1f1f1;
  --ink:#222426;
  --ink-soft:#555;
  --muted:#8a8a8a;
  --green:#6f9a3c;
  --green-text:#7aa84a;
  --chip:#e4e4e4;
  --rule:#d6d6d6;
  --danger:#e8605c;
  --white:#ffffff;
  --band-working:#e3ece0;
  --band-short:#efe3e3;
  --band-forgot:#d9e7ea;
}
*{box-sizing:border-box;margin:0;padding:0}
html,body{width:1200px;height:963px;overflow:hidden}
body{font-family:'Poppins',sans-serif;background:var(--page);color:var(--ink);position:relative}
.abs{position:absolute}

/* Header */
.topbar{left:0;top:0;width:1200px;height:54px;background:var(--topbar)}
.brand{left:22px;top:12px;color:var(--white);font-weight:600;font-size:20px;display:flex;align-items:center;gap:6px}
.brand svg{margin-top:3px}
.header-icon{top:15px}
.avatar{left:1111px;top:8px;width:39px;height:39px;border-radius:50%;background:linear-gradient(135deg,#8a6b58,#c9a48c)}
.avatar-caret{left:1157px;top:24px}

/* Main navigation rail */
.rail{left:0;top:54px;width:78px;height:909px;background:var(--rail)}
.rail-item{position:absolute;left:0;width:78px;text-align:center;color:var(--sidebar-text);font-size:9px;line-height:12px}
.rail-item .icon{display:flex;align-items:center;justify-content:center;margin:0 auto 5px;width:36px;height:36px}
.rail-item.active .icon{background:#e3e3e3;border-radius:50%}
.rail-divider{position:absolute;left:0;width:78px;height:1px;background:#3a3d40}

/* Vocabulary sidebar */
.vocab-nav{left:78px;top:54px;width:219px;height:909px;background:var(--sidebar);overflow:hidden}
.nav-select{left:39px;top:31px;width:111px;height:29px;border:1px solid #55585b;border-radius:3px;color:var(--sidebar-text);font-size:10px;padding:6px 12px;display:flex;justify-content:space-between;align-items:center}
.expand-btn{left:205px;top:33px;width:26px;height:26px;border-radius:6px;background:#3b3e41;display:flex;align-items:center;justify-content:center}
.nav-heading{left:38px;color:var(--sidebar-text);font-size:12px;font-weight:600;white-space:nowrap}
.nav-word-active{left:38px;top:113px;color:var(--green-text);font-size:9px;font-weight:700}
.nav-list{left:38px;top:188px;list-style:none;color:var(--sidebar-muted);font-size:10px;line-height:15px}
.nav-list li::before{content:"›";margin-right:6px}

/* Main content */
.stepper{left:300px;top:72px;width:560px;height:80px}
.step-label{position:absolute;top:0;width:80px;text-align:center;font-size:9px;font-weight:500;color:var(--ink-soft);letter-spacing:.3px}
.step-dot{position:absolute;top:20px;width:54px;height:54px;border-radius:50%;display:flex;align-items:center;justify-content:center}
.step-done{background:var(--green)}
.step-current{background:var(--ink)}
.step-todo{background:var(--white);border:2px solid var(--ink)}
.step-line{position:absolute;top:45px;height:4px}

.exercise-btn{left:930px;top:202px;width:232px;height:38px;border-radius:19px;background:var(--ink);color:var(--white);font-size:9.5px;font-weight:700;display:flex;align-items:center;justify-content:center;letter-spacing:.2px}
.story-card{left:337px;top:267px;width:825px;height:111px;background:var(--card);border-radius:14px}
.story-text{position:absolute;right:38px;top:20px;text-align:right;font-size:12px;line-height:19px;color:var(--ink-soft);white-space:nowrap}

.chart-card{left:337px;top:453px;width:825px;height:300px;background:var(--card);border-radius:14px}
.chart-card svg{position:absolute;left:0;top:0}
.analysis-title{left:336px;top:785px;font-size:21px;font-weight:600;color:var(--ink)}
.analysis-card{left:337px;top:826px;width:825px;height:96px;background:var(--card);border-radius:14px;padding:17px 26px;font-size:12px;line-height:19px;color:var(--ink-soft)}
.analysis-card b{color:var(--ink)}

/* Expanded vocabulary popup */
.modal{left:184px;top:132px;width:833px;height:383px;background:var(--white);border-radius:36px;box-shadow:0 12px 40px rgba(0,0,0,.18)}
.modal-close{left:801px;top:13px;width:31px;height:31px;border-radius:50%;background:var(--danger);display:flex;align-items:center;justify-content:center}
.modal-select{left:44px;top:31px;width:285px;height:35px;border:1.5px solid var(--ink);border-radius:3px;font-size:11px;padding:0 18px;display:flex;align-items:center;justify-content:space-between}
.modal-rule{left:42px;width:746px;height:1px;background:var(--rule)}
.group-title{left:43px;font-size:16.5px;font-weight:600;display:flex;align-items:center;gap:12px}
.help{width:14px;height:14px;border:1.3px solid var(--ink-soft);border-radius:50%;font-size:9px;font-weight:600;display:flex;align-items:center;justify-content:center;color:var(--ink-soft)}
.group-words{left:44px;display:flex;gap:7px}
.word-plain{font-size:10px;font-weight:700}
.chip{height:24px;background:var(--chip);border-radius:3px;font-size:10px;display:flex;align-items:center;justify-content:center;color:var(--ink)}
</style>
</head>
<body>

<!-- Header -->
<header class="abs topbar">
  <div class="abs brand">TopQuizLane
    <svg width="10" height="8" viewBox="0 0 10 8"><path d="M2 2l3 3 3-3" stroke="#fff" stroke-width="1.4" fill="none"/></svg>
  </div>
  <svg class="abs header-icon" style="left:1041px" width="22" height="22" viewBox="0 0 24 24" fill="none" stroke="#fff" stroke-width="1.6"><circle cx="12" cy="12" r="3.2"/><path d="M12 2.5l1.6 2.4 2.8-.8.6 2.8 2.8.6-.8 2.8 2.4 1.6-2.4 1.6.8 2.8-2.8.6-.6 2.8-2.8-.8L12 21.5l-1.6-2.4-2.8.8-.6-2.8-2.8-.6.8-2.8L2.5 12l2.4-1.6-.8-2.8 2.8-.6.6-2.8 2.8.8z"/></svg>
  <svg class="abs header-icon" style="left:1071px" width="22" height="22" viewBox="0 0 24 24" fill="none" stroke="#fff" stroke-width="1.6"><path d="M6 17V11a6 6 0 0112 0v6l2 2H4z"/><path d="M10 21h4"/></svg>
  <div class="abs avatar" role="img" aria-label="User account picture"></div>
  <svg class="abs avatar-caret" width="10" height="8" viewBox="0 0 10 8"><path d="M2 2l3 3 3-3" stroke="#fff" stroke-width="1.4" fill="none"/></svg>
</header>

<!-- Main navigation -->
<nav class="abs rail">
  <div class="rail-item active" style="top:24px">
    <div class="icon"><svg width="16" height="16" viewBox="0 0 24 24" fill="#2a2d30"><path d="M12 3l9 8h-3v9h-4v-6h-4v6H6v-9H3z"/></svg></div>
    TopQuiz<br>Lane
  </div>
  <div class="rail-divider" style="top:112px"></div>
  <div class="rail-item" style="top:130px">
    <div class="icon" style="height:22px"><svg width="14" height="18" viewBox="0 0 14 18" fill="#d0d0d0"><path d="M7 0a7 7 0 017 7c0 5-7 11-7 11S0 12 0 7a7 7 0 017-7zm0 4.5a2.5 2.5 0 100 5 2.5 2.5 0 000-5z"/></svg></div>
    Daily<br>English
  </div>
  <div class="rail-divider" style="top:202px"></div>
  <div class="rail-item" style="top:228px">
    <div class="icon" style="height:22px"><svg width="16" height="18" viewBox="0 0 16 18" fill="none" stroke="#d0d0d0" stroke-width="1.5"><rect x="2" y="1" width="12" height="16"/><path d="M5 4h2M9 4h2M5 7h2M9 7h2M5 10h2M9 10h2M6.5 17v-3h3v3"/></svg></div>
    Business
  </div>
</nav>

<!-- Vocabulary navigation -->
<aside class="abs vocab-nav">
  <div class="abs nav-select">ALL
    <svg width="8" height="6" viewBox="0 0 8 6"><path d="M1 1l3 3 3-3" stroke="#c9c9c9" stroke-width="1.2" fill="none"/></svg>
  </div>
  <div class="abs expand-btn"><svg width="12" height="12" viewBox="0 0 12 12" fill="none" stroke="#ddd" stroke-width="1.2"><path d="M5 1H1v10h10V7M7 1h4v4M11 1L6 6"/></svg></div>
  <div class="abs nav-heading" style="top:88px">Short-Term Memory</div>
  <div class="abs nav-word-active">GRAB</div>
  <div class="abs nav-heading" style="top:166px">Working Memory</div>
  <ul class="abs nav-list">
    <li>Cool Down</li><li>Crav</li><li>Go For</li><li>Go-To</li><li>In The Mood For</li><li>Sip</li><li>Soothing</li><li>Stick With</li><li>Throw In/Throw On</li>
  </ul>
  <div class="abs nav-heading" style="top:362px">Long-Term Memory</div>
  <ul class="abs nav-list" style="top:384px"><li>Give ItA Try</li></ul>
</aside>

<!-- Review progress -->
<section class="abs stepper">
  <div class="step-label" style="left:30px">REVIEW 1</div>
  <div class="step-label" style="left:173px">REVIEW 2</div>
  <div class="step-label" style="left:315px">REVIEW 3</div>
  <div class="step-label" style="left:462px">REVIEW 4</div>
  <div class="step-line" style="left:97px;width:116px;background:var(--ink)"></div>
  <div class="step-line" style="left:240px;width:270px;top:46px;height:2px;background:#cfcfcf"></div>
  <div class="step-dot step-done" style="left:43px"><svg width="22" height="18" viewBox="0 0 22 18"><path d="M2 9l6 6L20 3" stroke="#fff" stroke-width="3" fill="none"/></svg></div>
  <div class="step-dot step-current" style="left:186px"><svg width="20" height="22" viewBox="0 0 20 22" fill="#fff"><circle cx="10" cy="6" r="5"/><path d="M0 22a10 9 0 0120 0z"/></svg></div>
  <div class="step-dot step-todo" style="left:328px"></div>
  <div class="step-dot step-todo" style="left:475px"></div>
</section>

<div class="abs exercise-btn">VOCABULARY REVIEW EXERCISE 3</div>

<section class="abs story-card">
  <p class="story-text">Imagine it is a busy weekday morning and you are running late for<br>work. You leave the house in a hurry, and just before you reach the bus<br>stop, a friend hands you a hot coffee to go along. You <b>grab</b> it from</p>
</section>

<!-- Memory chart -->
<section class="abs chart-card">
  <svg width="825" height="300" viewBox="0 0 825 300" font-family="Poppins, sans-serif">
    <rect x="27" y="12" width="772" height="160" fill="var(--band-working)"/>
    <rect x="27" y="172" width="772" height="30" fill="var(--band-short)"/>
    <rect x="27" y="202" width="772" height="35" fill="var(--band-forgot)"/>
    <line x1="27" y1="237" x2="799" y2="237" stroke="#9a9a9a" stroke-width="1"/>
    <g font-size="8.5" fill="#8a8a8a">
      <text x="39" y="122">Working Memory</text>
      <text x="39" y="190">Short-Term Memory</text>
      <text x="39" y="222">Forgotten Memory</text>
    </g>
    <path d="M308 176 Q370 180 396 237" stroke="#777" stroke-dasharray="3 3" fill="none"/>
    <path d="M398 92 Q525 96 568 237" stroke="#777" stroke-dasharray="3 3" fill="none"/>
    <rect x="304" y="187" width="5" height="50" fill="var(--ink)"/>
    <rect x="394" y="90" width="5" height="147" fill="var(--ink)"/>
    <rect x="290" y="162" width="34" height="14" fill="#e4e4e4"/>
    <text x="307" y="172" font-size="7.5" text-anchor="middle" fill="#444">21 May</text>
    <rect x="379" y="64" width="34" height="14" fill="#e4e4e4"/>
    <text x="396" y="74" font-size="7.5" text-anchor="middle" fill="#444">22 May</text>
    <g font-size="7.5" fill="#666" text-anchor="middle">
      <text x="43" y="261">18 May</text><text x="87" y="261">12:00</text>
      <text x="131" y="261">19 May</text><text x="174" y="261">12:00</text>
      <text x="218" y="261">20 May</text><text x="262" y="261">12:00</text>
      <text x="306" y="261">21 May</text><text x="350" y="261">12:00</text>
      <text x="394" y="261">22 May</text><text x="437" y="261">12:00</text>
      <text x="481" y="261">23 May</text><text x="525" y="261">12:00</text>
      <text x="569" y="261">24 May</text><text x="613" y="261">12:00</text>
      <text x="656" y="261">25 May</text><text x="700" y="261">12:00</text>
      <text x="744" y="261">26 May</text><text x="788" y="261">12:00</text>
    </g>
    <text x="392" y="287" font-size="8.5" font-weight="600" text-anchor="middle" fill="#444">DATE RANGE</text>
  </svg>
</section>

<h2 class="abs analysis-title">TopQuizLane Learning Analysis</h2>
<section class="abs analysis-card">
  Lorem ipsum <b>dolor</b> sit amet, consectetur adipiscing elit. Nam <b>rutrum commodo</b> enim id bibendum. Nunc dignissim risus <b>dolor</b>nec finibus dictum eu. Aliquam sit amet euismod metus, quis malesuada erat. Sed at felis quis nulla feugiat cursus at at <b>dolor</b>. Maecenas pretium aliquet dapibus. Fusce et eleifend massa.&nbsp; Sed convallis ex mi, at lobortis ligula congue vel.
</section>

<!-- Expanded vocabulary popup -->
<div class="abs modal" role="dialog" aria-label="All vocabulary">
  <div class="abs modal-close"><svg width="12" height="12" viewBox="0 0 12 12"><path d="M2 2l8 8M10 2l-8 8" stroke="#fff" stroke-width="1.8"/></svg></div>
  <div class="abs modal-select">ALL
    <svg width="9" height="6" viewBox="0 0 9 6"><path d="M1 1l3.5 3.5L8 1" stroke="#222" stroke-width="1.3" fill="none"/></svg>
  </div>
  <div class="abs modal-rule" style="top:93px"></div>
  <div class="abs group-title" style="top:106px">Short-Term Memory <span class="help">?</span></div>
  <div class="abs group-words word-plain" style="top:141px">GRAB</div>
  <div class="abs modal-rule" style="top:173px"></div>
  <div class="abs group-title" style="top:187px">Working Memory <span class="help">?</span></div>
  <div class="abs group-words" style="top:225px">
    <span class="chip" style="width:68px">Cool Down</span>
    <span class="chip" style="width:65px">Crav</span>
    <span class="chip" style="width:66px">Go For</span>
    <span class="chip" style="width:65px">Go-To</span>
    <span class="chip" style="width:93px">In The Mood For</span>
    <span class="chip" style="width:60px">Sip</span>
    <span class="chip" style="width:72px">Soothing</span>
    <span class="chip" style="width:75px">Stick With</span>
    <span class="chip" style="width:117px">Throw In/Throw On</span>
  </div>
  <div class="abs modal-rule" style="top:272px"></div>
  <div class="abs group-title" style="top:285px">Long-Term Memory <span class="help">?</span></div>
  <div class="abs group-words" style="top:324px">
    <span class="chip" style="width:80px">Give ItA Try</span>
  </div>
</div>

</body>
</html>
```